Corporate Business card, Letter head, & Envelope
CorvaneLG
Professional
Nadia Perrow
CEO
5827 Fenwillow Dr, Suite 408
Brenmoor, Texas 75419
nadiap@corvaneloftsgroup.example
www.corvaneloftsgroup.example
We are a corporate travel management and not a leisure company, so we need to stay professional

```html
<!DOCTYPE html>
<html lang="en">
<head>
<meta charset="utf-8">
<title>CorvaneLG Business Card</title>
<link rel="stylesheet" href="https://fonts.googleapis.com/css2?family=Michroma&display=swap">
<style>
  :root {
    --page-bg: #e6e7ea;
    --card-top: #ffffff;
    --card-fade: #e4e6ea;
    --brand-blue: #2a3f9a;
    --deep-blue: #1c2a78;
    --accent-orange: #f49a1f;
    --ink-white: #ffffff;
  }
  html, body {
    margin: 0;
    padding: 0;
    width: 1200px;
    height: 770px;
    overflow: hidden;
    background: var(--page-bg);
  }
  .canvas { position: relative; width: 1200px; height: 770px; }
  .business-card {
    position: absolute;
    left: 80px;
    top: 73px;
    width: 1040px;
    height: 624px;
    border-radius: 42px;
    overflow: hidden;
    background: linear-gradient(180deg, var(--card-top) 0%, var(--card-top) 30%, var(--card-fade) 70%);
    box-shadow: 0 10px 28px rgba(20, 30, 60, 0.18);
    font-family: "Michroma", "Arial", sans-serif;
  }
  .card-waves { position: absolute; inset: 0; width: 100%; height: 100%; }
  .brand {
    position: absolute;
    left: 220px;
    top: 96px;
    display: flex;
    align-items: center;
    gap: 24px;
  }
  .brand-mark {
    width: 112px;
    height: 112px;
    border-radius: 50%;
    background: var(--brand-blue);
  }
  .brand-text { display: flex; flex-direction: column; gap: 14px; }
  .brand-name {
    margin: 0;
    font-size: 36px;
    font-weight: 400;
    letter-spacing: 2px;
    color: var(--brand-blue);
    line-height: 1;
  }
  .brand-tagline {
    margin: 0;
    font-size: 13px;
    letter-spacing: 1.2px;
    text-transform: uppercase;
    color: var(--accent-orange);
  }
  .contact-list {
    position: absolute;
    left: 36px;
    top: 420px;
    margin: 0;
    padding: 0;
    list-style: none;
    color: var(--ink-white);
    font-size: 12px;
    letter-spacing: 0.6px;
  }
  .contact-list li { display: flex; align-items: center; gap: 9px; height: 23px; }
  .contact-list .indent { padding-left: 25px; }
  .contact-icon { width: 16px; height: 16px; flex: none; }
  .contact-person {
    position: absolute;
    right: 32px;
    top: 496px;
    text-align: right;
    color: var(--ink-white);
    letter-spacing: 2px;
  }
  .person-name { margin: 0; font-size: 18px; font-weight: 400; }
  .person-title { margin: 8px 0 0; font-size: 18px; }
</style>
</head>
<body>
<div class="canvas">
  <div class="business-card">
    <svg class="card-waves" viewBox="0 0 1040 624" preserveAspectRatio="none" aria-hidden="true">
      <defs>
        <linearGradient id="blueBand" x1="0" y1="0" x2="1" y2="1">
          <stop offset="0" stop-color="#3a55c0"/>
          <stop offset="0.5" stop-color="#2a3f9a"/>
          <stop offset="1" stop-color="#1c2a78"/>
        </linearGradient>
        <linearGradient id="orangeSweep" x1="0" y1="0" x2="1" y2="0">
          <stop offset="0" stop-color="#f7b43a" stop-opacity="0"/>
          <stop offset="0.35" stop-color="#f7b43a"/>
          <stop offset="1" stop-color="#f08a12"/>
        </linearGradient>
      </defs>
      <path d="M180 372 C 420 300, 640 350, 820 300 C 920 272, 990 240, 1040 212 L1040 236 C 990 268, 920 300, 820 326 C 640 372, 420 330, 180 380 Z" fill="url(#orangeSweep)"/>
      <path d="M300 382 C 520 338, 700 378, 860 338 C 950 314, 1000 286, 1040 260 L1040 250 C 1000 276, 950 304, 860 326 C 700 366, 520 328, 300 382 Z" fill="url(#orangeSweep)" opacity="0.85"/>
      <path d="M0 352 C 220 320, 440 420, 700 384 C 860 362, 970 310, 1040 270 L1040 624 L0 624 Z" fill="url(#blueBand)"/>
      <path d="M0 352 C 220 320, 440 420, 700 384 C 860 362, 970 310, 1040 270" fill="none" stroke="#ffffff" stroke-opacity="0.35" stroke-width="3"/>
    </svg>

    <div class="brand">
      <div class="brand-mark"></div>
      <div class="brand-text">
        <h1 class="brand-name">CORVANELG</h1>
        <p class="brand-tagline">Travel Management Company</p>
      </div>
    </div>

    <ul class="contact-list">
      <li>
        <svg class="contact-icon" viewBox="0 0 16 16"><circle cx="8" cy="8" r="7.5" fill="#fff"/><path d="M8 3.5a2.6 2.6 0 0 0-2.6 2.6C5.4 8.2 8 12 8 12s2.6-3.8 2.6-5.9A2.6 2.6 0 0 0 8 3.5z" fill="#2a3f9a"/></svg>
        5827 Fenwillow Dr, Suite 408
      </li>
      <li class="indent">Brenmoor, Texas 75419</li>
      <li>
        <svg class="contact-icon" viewBox="0 0 16 16"><circle cx="8" cy="8" r="7.5" fill="#fff"/><path d="M5 4.5l1.6-.4 1 2.2-1 .8a5 5 0 0 0 2.3 2.3l.8-1 2.2 1-.4 1.6c-3.3.3-6.8-3.2-6.5-6.5z" fill="#2a3f9a"/></svg>
        800-555-0142
      </li>
      <li>
        <svg class="contact-icon" viewBox="0 0 16 16"><circle cx="8" cy="8" r="7.5" fill="#fff"/><path d="M5 4.5l1.6-.4 1 2.2-1 .8a5 5 0 0 0 2.3 2.3l.8-1 2.2 1-.4 1.6c-3.3.3-6.8-3.2-6.5-6.5z" fill="#2a3f9a"/></svg>
        972-555-0187
      </li>
      <li>
        <svg class="contact-icon" viewBox="0 0 16 16"><circle cx="8" cy="8" r="7.5" fill="#fff"/><path d="M5 4.5l1.6-.4 1 2.2-1 .8a5 5 0 0 0 2.3 2.3l.8-1 2.2 1-.4 1.6c-3.3.3-6.8-3.2-6.5-6.5z" fill="#2a3f9a"/></svg>
        972-555-0193
      </li>
      <li>
        <svg class="contact-icon" viewBox="0 0 16 16"><circle cx="8" cy="8" r="7.5" fill="#fff"/><rect x="4" y="5.2" width="8" height="5.6" fill="#2a3f9a"/><path d="M4 5.2l4 3 4-3" fill="none" stroke="#fff" stroke-width="0.8"/></svg>
        nadiap@corvaneloftsgroup.example
      </li>
      <li>
        <svg class="contact-icon" viewBox="0 0 16 16"><circle cx="8" cy="8" r="7.5" fill="#fff"/><circle cx="8" cy="8" r="4" fill="none" stroke="#2a3f9a" stroke-width="1"/><path d="M4 8h8M8 4c-1.8 2.4-1.8 5.6 0 8M8 4c1.8 2.4 1.8 5.6 0 8" fill="none" stroke="#2a3f9a" stroke-width="0.8"/></svg>
        www.corvaneloftsgroup.example
      </li>
    </ul>

    <div class="contact-person">
      <h2 class="person-name">Nadia Perrow</h2>
      <p class="person-title">CEO</p>
    </div>
  </div>
</div>
</body>
</html>
```